Design for Outdoor Sign/Banner to be used at Markets/Pop Up Events

We are a small boutique nursery based in Ferndale, QLD specialising in Platycerium species. We propagate, grow and sell the 18 different species of Platycerium. All of our Platyceriums are grown in shade houses on site and are hardened in natural conditions. We would like to see designs that use the colour green. I will attach our Company Logo and also the Stubbie Cooler Design that a designer created through Motif Harbour. Banner size would be approx 2 metres wide, 1 metre high.

```html
<!DOCTYPE html>
<html lang="en">
<head>
<meta charset="utf-8">
<title>Fernhollow Staghorns – Market Banner</title>
<link rel="stylesheet" href="https://fonts.googleapis.com/css2?family=Great+Vibes&family=Oswald:wght@300;400;600;700&family=Poppins:wght@500;600;700&display=swap">
<style>
  :root {
    --page-bg: #a9a9a9;
    --forest: #1f7a22;
    --forest-deep: #135c17;
    --charcoal: #262626;
    --lime: #c4ec8e;
    --lime-pale: #d9f3b8;
    --white: #ffffff;
    --wall-light: #eeeeee;
    --wall-mid: #d9d9d9;
    --hedge: #3f6b2c;
  }
  * { margin: 0; padding: 0; box-sizing: border-box; }
  html, body { width: 887px; height: 1200px; overflow: hidden; }
  body { background: var(--page-bg); position: relative; }

  .banner {
    position: absolute; left: 30px; top: 394px;
    width: 827px; height: 413px; overflow: hidden;
    box-shadow: 0 6px 18px rgba(0,0,0,.35);
  }
  .banner__art { position: absolute; inset: 0; }

  .headline-script {
    position: absolute; left: 20px; top: 8px;
    font-family: "Great Vibes", cursive; font-size: 70px; line-height: 1;
    color: var(--lime); transform: rotate(-3deg); transform-origin: left bottom;
    white-space: nowrap;
  }
  .headline-main {
    position: absolute; left: 26px; top: 76px;
    font-family: "Oswald", sans-serif; font-weight: 700; font-size: 38px;
    letter-spacing: -.5px; color: var(--white); line-height: 1; white-space: nowrap;
  }
  .species-pill {
    position: absolute; left: 26px; top: 133px; width: 355px; height: 26px;
    background: var(--charcoal); border-radius: 13px;
    font-family: "Poppins", sans-serif; font-weight: 700; font-size: 15px;
    color: var(--white); line-height: 26px; padding-left: 9px; white-space: nowrap;
  }

  .features { position: absolute; left: 11px; top: 174px; display: flex; list-style: none; }
  .feature {
    width: 104px; height: 92px; text-align: center; color: var(--white);
    font-family: "Poppins", sans-serif; font-weight: 600; font-size: 10.5px; line-height: 1.2;
    border-right: 1px solid rgba(255,255,255,.18);
  }
  .feature:last-child { border-right: none; }
  .feature__icon { display: block; margin: 0 auto 7px; width: 44px; height: 44px; }

  .badge-location {
    position: absolute; left: 331px; top: 177px; width: 134px; height: 84px;
    font-family: "Oswald", sans-serif; color: var(--forest-deep);
  }
  .badge-location__leaf { position: absolute; inset: 0; }
  .badge-location__lead {
    position: absolute; left: 10px; top: 14px; width: 114px; text-align: center;
    font-weight: 300; font-size: 12px; line-height: 1; white-space: nowrap;
  }
  .badge-location__place {
    position: absolute; left: 28px; top: 30px;
    font-weight: 700; font-size: 15px; line-height: 1.1; color: var(--forest);
    white-space: nowrap;
  }
  .badge-location__place .pin { width: 9px; height: 12px; margin-right: 4px; vertical-align: -1px; }
  .badge-location__place .indent { padding-left: 13px; }

  .brand-name {
    position: absolute; left: 22px; top: 318px; width: 96px;
    font-family: "Oswald", sans-serif; font-weight: 700; font-size: 17px; line-height: 1.1;
    color: var(--white); text-transform: uppercase; text-align: center;
  }
  .visit-line {
    position: absolute; left: 137px; top: 284px;
    font-family: "Oswald", sans-serif; font-weight: 300; font-size: 18px; line-height: 1.2;
    color: var(--white); letter-spacing: -.3px; white-space: nowrap;
  }
  .visit-line strong { font-weight: 600; color: var(--lime); }
  .address {
    position: absolute; left: 139px; top: 322px; padding-left: 14px;
    font-family: "Poppins", sans-serif; font-weight: 500; font-size: 12px; line-height: 1.3;
    color: var(--white); white-space: nowrap;
  }
  .address .pin { position: absolute; left: 0; top: 3px; width: 7px; height: 10px; }
  .phone {
    position: absolute; left: 279px; top: 318px;
    font-family: "Oswald", sans-serif; font-weight: 600; font-size: 29px; line-height: 1;
    color: var(--white); display: flex; align-items: center; gap: 9px; white-space: nowrap;
  }
  .phone svg { width: 21px; height: 21px; }
  .follow-bar { position: absolute; left: 134px; top: 368px; display: flex; height: 19px; }
  .follow-bar__label {
    background: var(--forest); color: var(--lime); width: 104px; border-radius: 3px 0 0 3px;
    font-family: "Poppins", sans-serif; font-weight: 700; font-size: 9.5px; line-height: 19px; text-align: center;
  }
  .follow-bar__url {
    background: var(--white); color: var(--charcoal); width: 262px; border-radius: 0 3px 3px 0;
    font-family: "Poppins", sans-serif; font-weight: 500; font-size: 9.5px; line-height: 19px; padding-left: 8px;
    white-space: nowrap; overflow: hidden;
  }
</style>
</head>
<body>
<main class="banner">
  <svg class="banner__art" viewBox="0 0 827 413" width="827" height="413">
    <defs>
      <linearGradient id="wallGradient" x1="0" y1="0" x2="0" y2="1">
        <stop offset="0" stop-color="var(--wall-light)"/>
        <stop offset=".82" stop-color="var(--wall-mid)"/>
        <stop offset=".84" stop-color="var(--hedge)"/>
        <stop offset="1" stop-color="#2f5520"/>
      </linearGradient>
      <linearGradient id="forestGradient" x1="0" y1="0" x2="1" y2="1">
        <stop offset="0" stop-color="#238326"/>
        <stop offset="1" stop-color="var(--forest-deep)"/>
      </linearGradient>
      <clipPath id="panelClip">
        <path d="M0 0 H445 C405 80 400 190 470 270 C495 300 505 360 505 413 H0 Z"/>
      </clipPath>
    </defs>
    <rect class="photo-area" x="0" y="0" width="827" height="413" fill="url(#wallGradient)" role="img" aria-label="Photo of mounted staghorn ferns on timber shields hung on a white brick wall above a low green hedge"/>
    <path class="panel-edge" d="M0 0 H455 C415 80 410 190 480 270 C505 300 515 360 515 413 H0 Z" fill="var(--lime-pale)"/>
    <g clip-path="url(#panelClip)">
      <rect class="panel-green" x="0" y="0" width="520" height="413" fill="url(#forestGradient)"/>
      <rect class="panel-dark" x="0" y="274" width="520" height="139" fill="var(--charcoal)"/>
    </g>
  </svg>

  <div class="headline-script">Discover the</div>
  <h1 class="headline-main">ART OF PLATYCERIUMS</h1>
  <div class="species-pill">18 DISTINCT SPECIES OF PLATYCERIUM</div>

  <ul class="features">
    <li class="feature">
      <svg class="feature__icon" viewBox="0 0 44 44"><rect x="5" y="5" width="34" height="34" fill="none" stroke="#fff" stroke-width="1.3"/><rect x="2" y="2" width="34" height="34" fill="none" stroke="rgba(255,255,255,.5)" stroke-width="1"/><path d="M22 12a7 7 0 0 0-7 7c0 5 7 12 7 12s7-7 7-12a7 7 0 0 0-7-7z" fill="none" stroke="#fff" stroke-width="1.8"/><circle cx="22" cy="19" r="2.6" fill="#fff"/><ellipse cx="22" cy="32" rx="8" ry="2" fill="none" stroke="#fff" stroke-width="1.3"/></svg>
      Locally<br>Propagated &amp;<br>Grown on Site
    </li>
    <li class="feature">
      <svg class="feature__icon" viewBox="0 0 44 44"><rect x="5" y="5" width="34" height="34" fill="none" stroke="#fff" stroke-width="1.3"/><rect x="2" y="2" width="34" height="34" fill="none" stroke="rgba(255,255,255,.5)" stroke-width="1"/><path d="M14 31c2-10 9-16 18-17-1 9-7 16-16 16" fill="#fff"/><path d="M13 33c3-6 7-10 13-13" stroke="var(--forest)" stroke-width="1.5" fill="none"/></svg>
      Hardened<br>in Natural<br>Conditions
    </li>
    <li class="feature">
      <svg class="feature__icon" viewBox="0 0 44 44"><rect x="5" y="5" width="34" height="34" fill="none" stroke="#fff" stroke-width="1.3"/><rect x="2" y="2" width="34" height="34" fill="none" stroke="rgba(255,255,255,.5)" stroke-width="1"/><path d="M11 22l11-10 11 10" fill="none" stroke="#fff" stroke-width="2.2"/><path d="M14 21v11h16V21" fill="none" stroke="#fff" stroke-width="2"/><path d="M22 30c-4-2-4-6 0-8 4 2 4 6 0 8z" fill="#fff"/></svg>
      Specialized<br>Shade House<br>Cultivation
    </li>
  </ul>

  <div class="badge-location">
    <svg class="badge-location__leaf" viewBox="0 0 134 84"><path d="M4 36C12 10 58 -2 104 6c14 3 24 12 28 24-2 32-40 54-86 54C20 84 0 62 4 36z" fill="var(--lime)"/></svg>
    <div class="badge-location__lead">BOUTIQUE NURSERY IN</div>
    <div class="badge-location__place"><svg class="pin" viewBox="0 0 10 14"><path d="M5 0a5 5 0 0 0-5 5c0 4 5 9 5 9s5-5 5-9a5 5 0 0 0-5-5z" fill="var(--forest-deep)"/><circle cx="5" cy="5" r="1.8" fill="var(--lime)"/></svg>FERNDALE,<br><span class="indent">QLD</span></div>
  </div>

  <div class="brand-name">Fernhollow Staghorns</div>

  <div class="visit-line">VISIT US TO EXPLORE <strong>OUR UNIQUE COLLECTION!</strong></div>
  <div class="address"><svg class="pin" viewBox="0 0 10 14"><path d="M5 0a5 5 0 0 0-5 5c0 4 5 9 5 9s5-5 5-9a5 5 0 0 0-5-5z" fill="var(--lime)"/><circle cx="5" cy="5" r="1.8" fill="var(--charcoal)"/></svg>Ferndale, QLD,<br>Australia, 4510</div>
  <div class="phone"><svg viewBox="0 0 24 24"><path d="M6.6 10.8a15 15 0 0 0 6.6 6.6l2.2-2.2c.3-.3.7-.4 1-.2 1.1.4 2.3.6 3.6.6.6 0 1 .4 1 1V20c0 .6-.4 1-1 1A17 17 0 0 1 3 4c0-.6.4-1 1-1h3.5c.6 0 1 .4 1 1 0 1.2.2 2.4.6 3.6.1.3 0 .7-.2 1z" fill="var(--lime)"/><path d="M14 3a7 7 0 0 1 7 7M14 6.5a3.5 3.5 0 0 1 3.5 3.5" stroke="var(--lime)" stroke-width="1.6" fill="none"/></svg>3600128455</div>
  <div class="follow-bar">
    <div class="follow-bar__label">FOLLOW US ON</div>
    <div class="follow-bar__url">https://www.social.example/fernhollowstaghorns</div>
  </div>
</main>
</body>
</html>
```